New Fun, Positive, energised looking Business Card Needed for High Achiever Coach

I am looking for a two sided full colour business card. I am self employed and have recently re branded my 1-2-1 work re-vitalising high achievers. My target client base for these cards is therefore high achievers - usually aged 40 -55, they are often entrepreneurs, CEO or work in banking and finance and 2/3 are male. I work with them on 90 day or 6 month coaching programs to help them live their success in a healthier, more sustainable and fulfiiled way. They pay for this privately so though they are corporate types the cards need not look 'corporate'. I want to portray the idea of transformation, vitality and re-connecting.
You can get a feel for the look I like on my new website: morvenlakey.co.uk
I want to use this logo with strapline (Re-Vitalising High Achievers) (I purchased off Markfolio) and font/ colours (the turquoise and green).
Details to include on the card:
www.morvenlakey.co.uk
+44 7913 264518
morven@morvenlakey.co.uk
skype: morvenlakey
I'd also like to include:
Do you struggle to switch off? Want to be healthier and feel fitter? Want closer relationships? More clarity over the direction you are headed? I can help you do these things using integrated mind-body techniques. Visit morvenlakey.co.uk TODAY to apply for a FREE Breakthrough session.
BUT if that is too much text for a card I am open to advice/ammendments.
Updates
Thanks for your design - I am considering them. PLease change the wording to :

```html
<!DOCTYPE html>
<html lang="en">
<head>
<meta charset="utf-8">
<title>Morven Lakey – Business Card</title>
<link rel="stylesheet" href="https://fonts.googleapis.com/css2?family=Open+Sans:wght@400;700;800&family=Dancing+Script:wght@500&display=swap">
<style>
  :root {
    --backdrop: #3c3c3c;
    --card-white: #ffffff;
    --card-shade: #eef0f1;
    --green: #55b45e;
    --turquoise: #0f8fb3;
    --turquoise-deep: #0a5f7d;
    --turquoise-light: #12a7cc;
    --ink: #1f1f1f;
    --muted-line: #1b93b8;
  }
  * { box-sizing: border-box; margin: 0; padding: 0; }
  html, body {
    width: 1200px; height: 900px; overflow: hidden;
    background: var(--backdrop);
    font-family: "Open Sans", Arial, sans-serif;
  }
  .canvas {
    width: 1200px; height: 900px;
    display: flex; flex-direction: column;
    align-items: center; justify-content: center; gap: 44px;
  }
  .card {
    position: relative;
    width: 680px; height: 388px;
    border-radius: 26px;
    overflow: hidden;
  }

  /* Front */
  .card-front {
    background: linear-gradient(160deg, var(--card-white) 55%, var(--card-shade));
  }
  .front-wave {
    position: absolute; top: 0; left: 0;
    width: 680px; height: 180px;
  }
  .brand-block {
    position: absolute; left: 44px; top: 96px;
    width: 300px;
    display: flex; flex-direction: column; align-items: center;
  }
  .brand-dot {
    width: 92px; height: 92px; border-radius: 50%;
    background: var(--green);
    margin-bottom: 22px;
  }
  .brand-name {
    font-weight: 800; font-size: 37px; line-height: 46px;
    letter-spacing: 0.3px; white-space: nowrap;
    color: var(--turquoise);
  }
  .strapline {
    font-family: "Dancing Script", cursive;
    font-size: 24px; line-height: 32px; white-space: nowrap;
    color: var(--turquoise);
  }
  .divider {
    position: absolute; left: 370px; top: 232px;
    width: 2px; height: 106px; background: var(--muted-line);
  }
  .contact-list {
    position: absolute; left: 394px; top: 234px;
    list-style: none;
    font-size: 17px; color: var(--ink); line-height: 26px;
    white-space: nowrap;
  }
  .contact-list li { display: flex; align-items: center; gap: 12px; }
  .contact-icon { width: 18px; height: 18px; flex: none; }

  /* Back */
  .card-back {
    background: radial-gradient(ellipse at 62% 30%, var(--turquoise-light) 0%, var(--turquoise) 45%, var(--turquoise-deep) 100%);
    color: #ffffff;
  }
  .back-brand {
    position: absolute; left: 0; right: 0; top: 70px;
    text-align: center;
    font-weight: 800; font-size: 46px; letter-spacing: 0.5px;
  }
  .back-pitch {
    position: absolute; left: 56px; right: 56px; top: 196px;
    text-align: center;
    font-size: 15.5px; line-height: 23px;
  }
  .back-pitch strong { font-weight: 700; display: block; }
</style>
</head>
<body>
<main class="canvas">

  <section class="card card-front" aria-label="Card front">
    <svg class="front-wave" viewBox="0 0 680 180" aria-hidden="true">
      <path d="M0,0 H680 V150 C560,150 470,84 330,69 C200,55 90,46 0,46 Z" fill="var(--green)"/>
      <path d="M0,58 C90,58 200,67 330,81 C470,96 560,162 680,162" fill="none" stroke="var(--turquoise)" stroke-width="7"/>
    </svg>

    <div class="brand-block">
      <div class="brand-dot" aria-hidden="true"></div>
      <h1 class="brand-name">Morven Lakey</h1>
      <p class="strapline">Re-Vitalising High Achievers</p>
    </div>

    <div class="divider" aria-hidden="true"></div>
    <ul class="contact-list">
      <li>
        <svg class="contact-icon" viewBox="0 0 24 24" aria-hidden="true"><path d="M6.6 10.8a15 15 0 0 0 6.6 6.6l2.2-2.2a1 1 0 0 1 1-.25 11.4 11.4 0 0 0 3.6.57 1 1 0 0 1 1 1V20a1 1 0 0 1-1 1A17 17 0 0 1 3 4a1 1 0 0 1 1-1h3.5a1 1 0 0 1 1 1c0 1.25.2 2.45.57 3.57a1 1 0 0 1-.25 1z" fill="var(--turquoise)"/></svg>
        +44 7913 264518
      </li>
      <li>
        <svg class="contact-icon" viewBox="0 0 24 24" aria-hidden="true"><g fill="none" stroke="var(--turquoise)" stroke-width="2"><circle cx="12" cy="12" r="9"/><ellipse cx="12" cy="12" rx="4" ry="9"/><path d="M3 12h18M5 7h14M5 17h14"/></g></svg>
        www.morvenlakey.co.uk
      </li>
      <li>
        <svg class="contact-icon" viewBox="0 0 24 24" aria-hidden="true"><rect x="2" y="5" width="20" height="14" rx="1.5" fill="var(--turquoise)"/><path d="M3 6l9 7 9-7" fill="none" stroke="#ffffff" stroke-width="1.6"/></svg>
        morven@morvenlakey.co.uk
      </li>
      <li>
        <svg class="contact-icon" viewBox="0 0 24 24" aria-hidden="true"><circle cx="12" cy="12" r="9" fill="var(--turquoise)"/></svg>
        morvenlakey
      </li>
    </ul>
  </section>

  <section class="card card-back" aria-label="Card back">
    <p class="back-brand">Morven Lakey</p>
    <p class="back-pitch">
      Do you struggle to switch off? Want to be healthier and feel fitter? Want closer relationships? More clarity over the direction you are headed? I can help you do these things using integrated mind-body techniques.
      <strong>Visit morvenlakey.co.uk TODAY to apply for a FREE Breakthrough session.</strong>
    </p>
  </section>

</main>
</body>
</html>
```